Kindle Grove Wording For Logo & Business card

I have the logo, I just need the "kindle Grove" wording to go with it, and a business card design. The only thing on the business card is the website info. We provide nature connection experiences, and bolster these efforts through writing and host a platform for community around it.

I also have an idea of what it could look like (sketch), though I'm really not sure how it would come out. I am open to the best design and happy to consider original artwork. You can see what the site is about at KindleGrove.com.

Contact Information for Business Card

The only thing on the business card is the website info and the design. I will put other messaging on the back.

Website lettering (KindleGrove.com) in Montserrat

Logo Text

Kindle Grove (letters optional)

Font styles to use
Other font styles liked:
• montserrat

```html
<!DOCTYPE html>
<html lang="en">
<head>
<meta charset="utf-8">
<title>Kindle Grove — Business Card</title>
<link rel="stylesheet" href="https://fonts.googleapis.com/css2?family=Montserrat:wght@500;800&display=swap">
<style>
  :root {
    --page-bg: #e9e8ec;
    --night: #140d26;
    --paper: #ffffff;
    --ember: #f39a12;
    --ember-deep: #e8661c;
    --plum: #35204a;
    --ink-light: #ffffff;
  }
  * { box-sizing: border-box; margin: 0; padding: 0; }
  html, body {
    width: 1200px;
    height: 900px;
    overflow: hidden;
    background: var(--page-bg);
    font-family: "Montserrat", Arial, sans-serif;
  }
  .sheet {
    width: 1200px;
    height: 900px;
    display: flex;
    flex-direction: column;
    align-items: center;
    justify-content: center;
    gap: 44px;
  }
  .card {
    width: 690px;
    height: 394px;
    border-radius: 26px;
    position: relative;
    display: flex;
    flex-direction: column;
    align-items: center;
    box-shadow: 0 6px 18px rgba(0,0,0,0.18);
  }
  .card--front { background: var(--night); }
  .card--back { background: var(--paper); }
  .wordmark {
    display: flex;
    align-items: center;
    gap: 18px;
    margin-top: 140px;
  }
  .wordmark__dot {
    width: 62px;
    height: 62px;
    border-radius: 50%;
    flex: none;
  }
  .wordmark__name {
    font-weight: 800;
    font-size: 60px;
    letter-spacing: 0.5px;
    line-height: 1;
  }
  .card--front .wordmark__dot { background: var(--ember-deep); }
  .card--front .wordmark__name { color: var(--ember); }
  .card--back .wordmark__dot { background: var(--night); }
  .card--back .wordmark__name { color: var(--plum); }
  .website {
    position: absolute;
    bottom: 70px;
    left: 0;
    right: 0;
    text-align: center;
    font-weight: 500;
    font-size: 19px;
    letter-spacing: 1px;
  }
  .card--front .website { color: var(--ink-light); }
  .card--back .website { color: var(--plum); }
</style>
</head>
<body>
  <main class="sheet">
    <section class="card card--front" aria-label="Card front">
      <div class="wordmark">
        <span class="wordmark__dot"></span>
        <span class="wordmark__name">Kindle Grove</span>
      </div>
      <p class="website">www.KindleGrove.com</p>
    </section>
    <section class="card card--back" aria-label="Card back">
      <div class="wordmark">
        <span class="wordmark__dot"></span>
        <span class="wordmark__name">Kindle Grove</span>
      </div>
      <p class="website">www.KindleGrove.com</p>
    </section>
  </main>
</body>
</html>
```